Brackenridge Strength Studio Chronic Pain Flyer

Double sided DL flyer required to promote a strength training studio to sufferers of chronic pain. Flyer will be displayed in osteopathy, chiropractic and massage clinics. Flyer should be clean, professional and appeal to an older (40+) demographic.

Target Market(s)

Chronic pain sufferers. Age 40+

Industry/Entity Type

Health And Wellness

Colors

Designer to choose colors to be used in the design.

Requirements
Must have
• See attached files for text copy and logo. Image(s) of people strength training with a coach or personal trainer, as well as images depicting pain in common parts of the body (such as those pictured in the supplied mock up)
• website address: brackenridgestrengthstudio.example.com.au
• phone number : 0452 918 304
• Street address: 4/63 Juniper Hollow Rd, Brackenridge
Nice to have
• Images such as in the attached files.

```html
<!DOCTYPE html>
<html lang="en">
<head>
<meta charset="utf-8">
<title>Brackenridge Strength Studio – Chronic Pain Flyer</title>
<link rel="stylesheet" href="https://fonts.googleapis.com/css2?family=Lato:wght@400;700;900&display=swap">
<style>
  :root{
    --board:#3a3a3a;
    --red:#d02027;
    --ink:#111111;
    --text:#1e1e1e;
    --grey:#9a9a9a;
    --logo-grey:#5a5e63;
    --white:#ffffff;
    --paper:#f7f7f7;
  }
  *{box-sizing:border-box;margin:0;padding:0}
  html,body{width:1200px;height:1200px;overflow:hidden;background:var(--board);font-family:'Lato',sans-serif}
  .board{position:relative;width:1200px;height:1200px}
  .flyer{position:absolute;width:443px;height:910px;background:var(--white);overflow:hidden;box-shadow:0 2px 6px rgba(0,0,0,.35)}
  .flyer--front{left:126px;top:126px}
  .flyer--back{left:637px;top:127px;background:var(--paper)}
  .shapes{position:absolute;left:0;top:0;width:443px;height:910px}
  .abs{position:absolute}

  .brand{position:absolute;left:0;width:100%;text-align:center;color:var(--logo-grey);font-weight:900;line-height:1;letter-spacing:1px}
  .brand__name{font-size:33px}
  .brand__sub{font-size:19px;letter-spacing:3px;margin-top:4px}

  .photo{position:absolute;left:0;top:150px;width:443px;height:470px;
    background:linear-gradient(160deg,#aab0c4 0%,#8f93b3 35%,#6d7aa8 60%,#c9a091 80%,#7a5a55 100%)}

  .headline{position:absolute;left:0;width:100%;text-align:center;line-height:1}
  .headline__small{font-weight:700;font-size:42px;letter-spacing:-.5px}
  .headline__big{font-weight:900;font-size:74px;letter-spacing:-1px;margin-top:4px}
  .flyer--front .headline{top:630px;color:var(--white)}
  .flyer--back .headline{top:37px;color:var(--ink)}

  .contact{position:absolute;left:0;width:100%}
  .contact__row{position:absolute;display:flex;align-items:center;white-space:nowrap}
  .contact__phone{font-weight:900;font-size:36px;letter-spacing:-.5px}
  .contact__line{font-size:17px}
  .flyer--front .contact__phone{color:var(--red)}
  .flyer--front .contact__line{color:var(--text)}
  .flyer--back .contact__phone,.flyer--back .contact__line{color:var(--white)}
  .icon{flex:none;margin-right:8px}

  .tagline{position:absolute;left:0;top:167px;width:100%;height:47px;background:var(--red);color:var(--white);
    font-weight:700;font-size:29px;text-align:center;line-height:47px;letter-spacing:-.3px}
  .copy{position:absolute;left:26px;width:392px;font-size:20px;line-height:25px;text-align:justify;color:var(--text)}
  .copy--intro{top:225px}
  .copy--studio{top:486px}

  .pain-spot{position:absolute;top:342px;width:125px;height:125px;border-radius:50%;border:3px solid var(--red);
    background:radial-gradient(circle at 50% 62%,#e9555b 0%,#d9a3a5 20%,#c8c8c8 42%,#eaeaea 80%,#ffffff 100%)}
  .pain-spot--back{left:13px}
  .pain-spot--shoulder{left:155px;background:radial-gradient(circle at 52% 40%,#e9555b 0%,#d9a3a5 20%,#bdbdbd 45%,#e4e4e4 85%,#fff 100%)}
  .pain-spot--knee{left:297px;background:radial-gradient(circle at 45% 55%,#e9555b 0%,#d9a3a5 18%,#b5b5b5 45%,#e2e2e2 85%,#fff 100%)}

  .label{position:absolute;top:1075px;color:var(--white);font-size:40px;font-weight:400;transform:translateX(-50%)}
</style>
</head>
<body>
<main class="board">

  <!-- FRONT -->
  <section class="flyer flyer--front">
    <div class="photo" role="img" aria-label="Photo of a female coach guiding an older man through a resistance band stretch in the studio"></div>
    <svg class="shapes" viewBox="0 0 443 910" aria-hidden="true">
      <path d="M0 0H443V158Q230 196 0 168Z" fill="#ffffff"/>
      <path d="M0 530Q210 615 443 535V910H0Z" fill="#9c9c9c"/>
      <path d="M0 550Q210 632 443 552V910H0Z" fill="#d02027"/>
      <rect x="0" y="760" width="443" height="126" fill="#ffffff"/>
      <rect x="0" y="886" width="443" height="24" fill="#d02027"/>
    </svg>
    <div class="brand" style="top:84px">
      <div class="brand__name">BRACKENRIDGE</div>
      <div class="brand__sub">STRENGTH STUDIO</div>
    </div>
    <h1 class="headline">
      <div class="headline__small">HEALTH THROUGH</div>
      <div class="headline__big">STRENGTH</div>
    </h1>
    <div class="contact" style="top:0">
      <div class="contact__row" style="left:64px;top:770px">
        <svg class="icon" width="36" height="36" viewBox="0 0 36 36"><circle cx="18" cy="18" r="16.5" fill="none" stroke="#9a9a9a" stroke-width="2"/><path d="M12 10c1-1 2-1 3 0l2 3c.6 1 .4 2-.4 2.6l-1 .8c.8 2 2.3 3.6 4.4 4.6l.8-1c.7-.8 1.7-1 2.6-.4l3 2c1 .7 1 1.8 0 2.8-1.5 1.5-3.4 1.8-5.3.9-4.2-2-7.3-5.1-9.2-9.4-.8-1.9-.4-3.6.9-4.9z" fill="#9a9a9a"/></svg>
        <span class="contact__phone">0452 918 304</span>
      </div>
      <div class="contact__row" style="left:74px;top:826px">
        <svg class="icon" width="20" height="20" viewBox="0 0 20 20"><g fill="none" stroke="#8a8a8a" stroke-width="1.4"><circle cx="10" cy="10" r="8.5"/><ellipse cx="10" cy="10" rx="3.8" ry="8.5"/><path d="M1.5 10h17M3 5.5h14M3 14.5h14"/></g></svg>
        <span class="contact__line">brackenridgestrengthstudio.example.com.au</span>
      </div>
      <div class="contact__row" style="left:78px;top:860px">
        <svg class="icon" width="16" height="20" viewBox="0 0 16 20"><path d="M8 0C3.6 0 0 3.4 0 7.7 0 13 8 20 8 20s8-7 8-12.3C16 3.4 12.4 0 8 0zm0 10.5A3 3 0 1 1 8 4.5a3 3 0 0 1 0 6z" fill="#8a8a8a"/></svg>
        <span class="contact__line">4/63 Juniper Hollow Rd, Brackenridge</span>
      </div>
    </div>
  </section>

  <!-- BACK -->
  <section class="flyer flyer--back">
    <svg class="shapes" viewBox="0 0 443 910" aria-hidden="true">
      <path d="M0 679Q220 770 443 677V910H0Z" fill="#a3a3a3"/>
      <path d="M0 700Q215 792 443 690V910H0Z" fill="#d02027"/>
    </svg>
    <h2 class="headline">
      <div class="headline__small">HEALTH THROUGH</div>
      <div class="headline__big">STRENGTH</div>
    </h2>
    <p class="tagline">You Don’t have to live in pain.</p>
    <p class="copy copy--intro">Strength taining has been shown to improve many chronic pain conditions and is now being routinely recommended by medical and health professionals.</p>
    <div class="pain-spot pain-spot--back" role="img" aria-label="Illustration of lower back pain highlighted in red"></div>
    <div class="pain-spot pain-spot--shoulder" role="img" aria-label="Illustration of shoulder pain highlighted in red"></div>
    <div class="pain-spot pain-spot--knee" role="img" aria-label="Illustration of knee pain highlighted in red"></div>
    <p class="copy copy--studio">Our private studio provides high quality strength training by expert strength coaches. We’ve helped countless people improve or eliminate chronic pain, contact us today and find out how we can help you.</p>
    <div class="brand" style="top:664px">
      <div class="brand__name">BRACKENRIDGE</div>
      <div class="brand__sub">STRENGTH STUDIO</div>
    </div>
    <div class="contact" style="top:0">
      <div class="contact__row" style="left:68px;top:776px">
        <svg class="icon" width="36" height="36" viewBox="0 0 36 36"><circle cx="18" cy="18" r="16.5" fill="none" stroke="#ffffff" stroke-width="2"/><path d="M12 10c1-1 2-1 3 0l2 3c.6 1 .4 2-.4 2.6l-1 .8c.8 2 2.3 3.6 4.4 4.6l.8-1c.7-.8 1.7-1 2.6-.4l3 2c1 .7 1 1.8 0 2.8-1.5 1.5-3.4 1.8-5.3.9-4.2-2-7.3-5.1-9.2-9.4-.8-1.9-.4-3.6.9-4.9z" fill="#ffffff"/></svg>
        <span class="contact__phone">0452 918 304</span>
      </div>
      <div class="contact__row" style="left:76px;top:828px">
        <svg class="icon" width="20" height="20" viewBox="0 0 20 20"><g fill="none" stroke="#ffffff" stroke-width="1.4"><circle cx="10" cy="10" r="8.5"/><ellipse cx="10" cy="10" rx="3.8" ry="8.5"/><path d="M1.5 10h17M3 5.5h14M3 14.5h14"/></g></svg>
        <span class="contact__line">brackenridgestrengthstudio.example.com.au</span>
      </div>
      <div class="contact__row" style="left:80px;top:855px">
        <svg class="icon" width="16" height="20" viewBox="0 0 16 20"><path d="M8 0C3.6 0 0 3.4 0 7.7 0 13 8 20 8 20s8-7 8-12.3C16 3.4 12.4 0 8 0zm0 10.5A3 3 0 1 1 8 4.5a3 3 0 0 1 0 6z" fill="#ffffff"/></svg>
        <span class="contact__line">4/63 Juniper Hollow Rd, Brackenridge</span>
      </div>
    </div>
  </section>

  <span class="label" style="left:327px">Front</span>
  <span class="label" style="left:845px">Back</span>
</main>
</body>
</html>
```